Custom unique Stationary design for Logistics company

We need a custom, unique , elegant and luxurious full stationary design using our new logo, following these guidelines:
1- Business card: double sided, both sides uses the navy blue as the background main color (same as the code of the navy blue used in our logo).
2- envelope and folder: also use the same navy blue as the main background color.
3- book cover( notepad cover) : same thing with the navy blue
4- letterhead: feel free to use the combination of the colors in our logo.
5- rest of the items are up to your creativity

Target Market(s)

corporates and other businesses

Industry/Entity Type

Logistics and heavy machines contractors

Requirements
Must have
• Letterhead, business card, envelope, notepad cover, paper, file
Nice to have
• navy blue to be main background color for business card, envelope, notepad cover

```html
<!DOCTYPE html>
<html lang="en">
<head>
<meta charset="utf-8">
<title>Norvale Freight – Stationery Set</title>
<link href="https://fonts.googleapis.com/css2?family=Montserrat:wght@400;500;600;700;800&family=Great+Vibes&display=swap" rel="stylesheet">
<style>
  :root{
    --navy:#0d4f78;
    --navy-deep:#0a4166;
    --orange:#e8582a;
    --paper:#ffffff;
    --canvas:#e6e6e6;
    --ink:#4a4a4a;
    --rule:#9aa7b2;
  }
  *{box-sizing:border-box;margin:0;padding:0}
  html,body{width:1200px;height:4397px;overflow:hidden}
  body{position:relative;background:var(--canvas);font-family:"Montserrat",sans-serif;color:var(--ink)}
  .section{position:absolute;left:0;width:1200px}
  .section--cards{top:0;height:840px;background:linear-gradient(180deg,#d9d9d9 0%,#8d8d8d 55%,#3a3a3a 100%)}
  .section--letter{top:840px;height:870px;background:#e4e4e4}
  .section--envelope{top:1710px;height:790px;background:#e9e9e9}
  .section--folder{top:2500px;height:1150px;background:#ececec}
  .section--notepad{top:3650px;height:747px;background:#e2e2e2}

  .sheet{position:absolute;overflow:hidden;box-shadow:0 10px 28px rgba(0,0,0,.22)}
  .sheet--white{background:var(--paper)}
  .sheet--navy{background:var(--navy)}
  .wave{position:absolute;left:0;bottom:0;width:100%}
  .wave .fill{fill:var(--navy)}
  .wave .line{fill:none;stroke:var(--orange);stroke-width:4}

  .brand{position:absolute;display:flex;align-items:center;gap:10px}
  .brand-dot{border-radius:50%;background:var(--orange);flex:none}
  .brand-name{font-weight:800;letter-spacing:.02em;line-height:1;white-space:nowrap}
  .brand-name--stacked{line-height:1.1}
  .brand--navy .brand-name{color:var(--navy)}
  .brand--white .brand-name{color:#fff}

  /* business cards */
  .card{width:540px;height:310px}
  .card--front{left:70px;top:90px}
  .card--back{left:590px;top:440px;border-bottom:5px solid var(--orange)}
  .card-divider{position:absolute;left:236px;top:36px;width:2px;height:170px;background:var(--navy)}
  .card-contact{position:absolute;left:256px;top:34px;font-size:13px;line-height:1.6;color:#333}
  .card-name{font-size:20px;font-weight:700;color:var(--orange)}
  .card-name b{color:var(--navy)}
  .card-role{font-size:14px;margin-bottom:6px}
  .icon-row{display:flex;align-items:center;gap:7px}
  .icon{width:12px;height:12px;flex:none}
  .icon path,.icon circle,.icon rect{fill:none;stroke:var(--navy);stroke-width:1.6}

  /* letterhead */
  .letter{left:290px;top:40px;width:620px;height:800px}
  .letter-rule{position:absolute;left:48px;right:48px;top:122px;height:2px;background:#5d86a4}
  .letter-address{position:absolute;right:48px;top:36px;font-size:9px;line-height:1.6;text-align:right;border-left:2px solid var(--navy);padding-left:10px}
  .letter-body{position:absolute;left:48px;right:60px;top:150px;font-size:10.5px;line-height:1.75;color:#555}
  .letter-body p{margin-bottom:12px}
  .letter-body .greet{font-weight:700;color:#333}
  .signature{font-family:"Great Vibes",cursive;font-size:26px;color:#333;margin-top:4px}

  /* envelope */
  .envelope{width:680px;height:340px}
  .envelope--back{left:460px;top:40px}
  .envelope--front{left:80px;top:390px}
  .env-address{position:absolute;left:40px;top:90px;font-size:11px;line-height:1.5;color:#333;font-weight:500}

  /* folder */
  .folder-open{position:absolute;left:150px;width:900px;height:500px;display:flex;box-shadow:0 12px 30px rgba(0,0,0,.22)}
  .folder-open--outside{top:50px}
  .folder-open--inside{top:600px}
  .panel{position:relative;width:450px;height:100%;overflow:hidden}
  .panel--navy{background:var(--navy)}
  .panel--white{background:var(--paper)}
  .panel--inner{background:#f4f4f4}
  .folder-footer{position:absolute;left:40px;bottom:30px;font-size:10px;color:#fff;line-height:1.9}
  .folder-footer .icon path,.folder-footer .icon circle,.folder-footer .icon rect{stroke:#fff}
  .pocket{position:absolute;left:0;right:0;bottom:0;height:150px;background:var(--navy)}
  .insert{position:absolute;left:40px;top:28px;width:370px;height:430px;background:#fff;box-shadow:0 2px 8px rgba(0,0,0,.15)}
  .insert-body{position:absolute;left:28px;right:28px;top:110px;font-size:8.5px;line-height:1.7;color:#555}
  .insert-body p{margin-bottom:8px}

  /* notepad */
  .notepad{top:50px;width:420px;height:640px}
  .notepad--cover{left:150px}
  .notepad--paper{left:630px}
  .notepad-date{position:absolute;right:36px;top:66px;font-size:12px;color:#444}
  .notepad-lines{position:absolute;left:34px;right:34px;top:100px}
  .notepad-lines span{display:block;height:1px;background:var(--rule);margin-bottom:25px}
</style>
</head>
<body>

<!-- Business cards -->
<section class="section section--cards">
  <div class="sheet sheet--white card card--front">
    <div class="brand brand--navy" style="left:36px;top:92px">
      <span class="brand-dot" style="width:18px;height:18px"></span>
      <span class="brand-name brand-name--stacked" style="font-size:26px">NORVALE<br>FREIGHT</span>
    </div>
    <div class="card-divider"></div>
    <div class="card-contact">
      <div class="card-name">DANIEL <b>OKAFOR</b></div>
      <div class="card-role">Co-Founder</div>
      <div>418 Harbourline Ave, Suite 9,</div>
      <div>Eastport, ON K7P 3R4</div>
      <div class="icon-row"><svg class="icon" viewBox="0 0 12 12"><path d="M2 1h3l1 3-2 1a7 7 0 003 3l1-2 3 1v3c-6 0-10-4-10-9z"/></svg>011 482 7031</div>
      <div class="icon-row"><svg class="icon" viewBox="0 0 12 12"><rect x="1" y="2.5" width="10" height="7"/><path d="M1 3l5 4 5-4"/></svg>hello@norvalefreight.com</div>
      <div class="icon-row"><svg class="icon" viewBox="0 0 12 12"><circle cx="6" cy="6" r="5"/><path d="M1 6h10M6 1c-3 3-3 7 0 10M6 1c3 3 3 7 0 10"/></svg>www.norvalefreight.com</div>
    </div>
    <svg class="wave" viewBox="0 0 540 310" height="310" preserveAspectRatio="none">
      <path class="fill" d="M0 270 C180 270 330 300 540 236 L540 310 L0 310Z"/>
      <path class="line" d="M0 258 C180 258 330 288 540 224"/>
    </svg>
  </div>
  <div class="sheet sheet--navy card card--back">
    <div class="brand brand--white" style="left:80px;top:130px">
      <span class="brand-dot" style="width:24px;height:24px"></span>
      <span class="brand-name" style="font-size:38px">NORVALE FREIGHT</span>
    </div>
  </div>
</section>

<!-- Letterhead -->
<section class="section section--letter">
  <div class="sheet sheet--white letter">
    <div class="brand brand--navy" style="left:48px;top:56px">
      <span class="brand-dot" style="width:16px;height:16px"></span>
      <span class="brand-name" style="font-size:24px">NORVALE FREIGHT</span>
    </div>
    <div class="letter-address">
      418 Harbourline Ave, Suite 9<br>Eastport, ON K7P 3R4<br>011 482 7031<br>hello@norvalefreight.com<br>www.norvalefreight.com
    </div>
    <div class="letter-rule"></div>
    <div class="letter-body">
      <p>January 03, 2030</p>
      <p>Ms. Jane Harlow<br>Project Manager<br>Unit 12, Harbor Road<br>Cityname, 10021</p>
      <p class="greet">Dear Ms. Harlow,</p>
      <p>Thank you for your continued trust in our team. We are pleased to confirm the schedule for your upcoming heavy equipment transfer and related site support services.</p>
      <p>Our crews will arrive early to prepare loading zones, check permits and coordinate escorts along the planned route.</p>
      <p>Please let us know if any details change before dispatch.</p>
      <p>Regards,</p>
      <div class="signature">Laura Bennett</div>
    </div>
    <svg class="wave" viewBox="0 0 620 200" height="200" preserveAspectRatio="none">
      <path class="fill" d="M0 120 C200 130 420 170 620 160 L620 200 L0 200Z"/>
      <path class="line" d="M0 106 C200 118 420 158 620 148"/>
    </svg>
  </div>
</section>

<!-- Envelope -->
<section class="section section--envelope">
  <div class="sheet sheet--navy envelope envelope--back">
    <div class="brand brand--white" style="left:150px;top:140px">
      <span class="brand-dot" style="width:20px;height:20px"></span>
      <span class="brand-name" style="font-size:34px">NORVALE FREIGHT</span>
    </div>
  </div>
  <div class="sheet sheet--white envelope envelope--front">
    <div class="brand brand--navy" style="left:40px;top:40px">
      <span class="brand-dot" style="width:16px;height:16px"></span>
      <span class="brand-name" style="font-size:24px">NORVALE FREIGHT</span>
    </div>
    <div class="env-address">418 Harbourline Ave, Suite 9<br>Eastport, ON K7P 3R4</div>
    <svg class="wave" viewBox="0 0 680 340" height="340" preserveAspectRatio="none">
      <path class="fill" d="M0 150 C220 180 430 250 680 340 L0 340Z"/>
      <path class="line" d="M0 134 C220 166 440 238 680 326"/>
    </svg>
  </div>
</section>

<!-- Folder -->
<section class="section section--folder">
  <div class="folder-open folder-open--outside">
    <div class="panel panel--navy">
      <div class="brand brand--white" style="left:60px;top:90px">
        <span class="brand-dot" style="width:16px;height:16px"></span>
        <span class="brand-name" style="font-size:28px">NORVALE FREIGHT</span>
      </div>
      <div class="folder-footer">
        <div>418 Harbourline Ave, Suite 9, Eastport, ON K7P 3R4</div>
        <div class="icon-row">
          <svg class="icon" viewBox="0 0 12 12"><path d="M2 1h3l1 3-2 1a7 7 0 003 3l1-2 3 1v3c-6 0-10-4-10-9z"/></svg>011 482 7031
          <svg class="icon" viewBox="0 0 12 12"><rect x="1" y="2.5" width="10" height="7"/><path d="M1 3l5 4 5-4"/></svg>hello@norvalefreight.com
          <svg class="icon" viewBox="0 0 12 12"><circle cx="6" cy="6" r="5"/><path d="M1 6h10M6 1c-3 3-3 7 0 10M6 1c3 3 3 7 0 10"/></svg>www.norvalefreight.com
        </div>
      </div>
    </div>
    <div class="panel panel--white">
      <div class="brand brand--navy" style="left:60px;top:50px">
        <span class="brand-dot" style="width:16px;height:16px"></span>
        <span class="brand-name" style="font-size:28px">NORVALE FREIGHT</span>
      </div>
      <svg class="wave" viewBox="0 0 450 140" height="140" preserveAspectRatio="none">
        <path class="fill" d="M0 110 C150 110 300 95 450 70 L450 140 L0 140Z"/>
        <path class="line" d="M0 98 C150 98 300 84 450 58"/>
      </svg>
    </div>
  </div>

  <div class="folder-open folder-open--inside">
    <div class="panel panel--inner">
      <div class="pocket"></div>
    </div>
    <div class="panel panel--inner">
      <div class="insert">
        <div class="brand brand--navy" style="left:28px;top:30px">
          <span class="brand-dot" style="width:12px;height:12px"></span>
          <span class="brand-name" style="font-size:17px">NORVALE FREIGHT</span>
        </div>
        <div class="insert-body">
          <p><b>Dear Ms. Harlow,</b></p>
          <p>Thank you for your continued trust in our team. We are pleased to confirm the schedule for your upcoming heavy equipment transfer and related site support services.</p>
          <p>Please let us know if any details change before dispatch.</p>
        </div>
      </div>
      <div class="pocket"></div>
    </div>
  </div>
</section>

<!-- Notepad -->
<section class="section section--notepad">
  <div class="sheet sheet--navy notepad notepad--cover">
    <div class="brand brand--white" style="left:50px;top:300px">
      <span class="brand-dot" style="width:16px;height:16px"></span>
      <span class="brand-name" style="font-size:28px">NORVALE FREIGHT</span>
    </div>
  </div>
  <div class="sheet sheet--white notepad notepad--paper">
    <div class="brand brand--navy" style="left:34px;top:30px">
      <span class="brand-dot" style="width:12px;height:12px"></span>
      <span class="brand-name" style="font-size:18px">NORVALE FREIGHT</span>
    </div>
    <div class="notepad-date">Date:..................</div>
    <div class="notepad-lines">
      <span></span><span></span><span></span><span></span><span></span><span></span><span></span><span></span><span></span><span></span><span></span><span></span><span></span><span></span><span></span><span></span><span></span><span></span>
    </div>
    <svg class="wave" viewBox="0 0 420 60" height="60" preserveAspectRatio="none">
      <path class="fill" d="M0 42 C140 40 280 36 420 24 L420 60 L0 60Z"/>
      <path class="line" d="M0 32 C140 30 280 26 420 14"/>
    </svg>
  </div>
</section>

</body>
</html>
```